Letterhead That Inspires Trust

Birchwell Deed Services, LLC, (BDS) fixes technical problems with property deeds. The problems usually surface when someone tries to buy, sell or mortgage a piece of real estate and one of the lawyers involved find a title defect (a lien, an undischarged mortgage, a deceased person still on the title, unpaid taxes, etc.). BDS then gets involved and often has to contact prior property owners to get them to sign paperwork fixing the problem. We need a letterhead that will a) convey the seriousness of what we are trying to do, b) cause the recipients of our letters to recognize the importance of what are trying to do, and c) convey that we are a established and trustworthy company. We want it to include an image that suggests we are a problem solving company. Attached is an image we think might work; you can use it or not. In addition to our name (Birchwell Deed Services, LLC), the letterhead must include our address and phone number: 418 Harlow Avenue, Suite 207, Providence, RI 02915 (401) 555-3726. We are thinking something straightforward without unnecessary colors or graphics.

```html
<!DOCTYPE html>
<html lang="en">
<head>
<meta charset="UTF-8">
<title>Birchwell Deed Services, LLC — Letterhead</title>
<link href="https://fonts.googleapis.com/css2?family=Barlow:wght@400;600&family=Montserrat:wght@400&display=swap" rel="stylesheet">
<style>
  :root {
    --backdrop: #e4e4e4;
    --paper: #ffffff;
    --brand-green: #3b7431;
    --ink: #3a3a3a;
    --ink-soft: #4a4a4a;
    --figure-wood: #e8cfb0;
    --figure-green: #6cbf3e;
  }
  * { margin: 0; padding: 0; box-sizing: border-box; }
  html, body {
    width: 1200px;
    height: 1200px;
    overflow: hidden;
    background: var(--backdrop);
  }
  .sheet {
    position: absolute;
    left: 190px;
    top: 20px;
    width: 820px;
    height: 1160px;
    background: var(--paper);
    font-family: "Barlow", Arial, sans-serif;
    color: var(--ink);
  }
  .brand-name {
    position: absolute;
    left: 50px;
    top: 62px;
    font-family: "Barlow", Arial, sans-serif;
    font-weight: 600;
    font-size: 33px;
    line-height: 36px;
    text-transform: uppercase;
    letter-spacing: 0.5px;
    color: var(--brand-green);
  }
  .contact {
    position: absolute;
    left: 584px;
    top: 83px;
    height: 56px;
    padding-left: 10px;
    border-left: 1.5px solid var(--brand-green);
    font-family: "Montserrat", Arial, sans-serif;
    font-size: 13.5px;
    line-height: 18px;
    color: var(--ink-soft);
  }
  .contact .phone {
    margin-top: 3px;
    display: flex;
    align-items: center;
    gap: 3px;
  }
  .recipient {
    position: absolute;
    left: 50px;
    top: 283px;
    font-size: 16px;
    line-height: 22px;
    letter-spacing: 0.3px;
  }
  .salutation {
    position: absolute;
    left: 50px;
    top: 437px;
    font-size: 16px;
    letter-spacing: 0.3px;
  }
  .letter-body {
    position: absolute;
    left: 50px;
    top: 481px;
    width: 717px;
    font-size: 16px;
    line-height: 22px;
    letter-spacing: 0.3px;
    text-align: justify;
  }
  .signature {
    position: absolute;
    left: 50px;
    top: 860px;
    width: 142px;
    height: 72px;
    background: linear-gradient(180deg, #ffffff 0%, #f1f1f1 50%, #ffffff 100%);
  }
  .closing {
    position: absolute;
    left: 50px;
    top: 944px;
    font-size: 16px;
    letter-spacing: 0.3px;
  }
  .problem-solving-image {
    position: absolute;
    left: 555px;
    top: 982px;
    width: 242px;
    height: 153px;
    background: radial-gradient(ellipse at 50% 60%, var(--figure-green) 0%, #c9e3b2 18%, var(--figure-wood) 40%, #f6efe6 70%, #ffffff 100%);
  }
</style>
</head>
<body>
  <main class="sheet">
    <header>
      <div class="brand-name">Birchwell Deed<br>Services, LLC</div>
      <address class="contact" style="font-style: normal;">
        <div>418 Harlow Avenue, Suite 207,</div>
        <div>Providence, RI 02915</div>
        <div class="phone">
          <svg width="11" height="11" viewBox="0 0 24 24" aria-hidden="true">
            <path fill="#3b7431" d="M6.6 10.8c1.4 2.8 3.8 5.1 6.6 6.6l2.2-2.2c.3-.3.7-.4 1-.2 1.1.4 2.3.6 3.6.6.6 0 1 .4 1 1V20c0 .6-.4 1-1 1C10.6 21 3 13.4 3 4c0-.6.4-1 1-1h3.5c.6 0 1 .4 1 1 0 1.3.2 2.5.6 3.6.1.3 0 .7-.2 1L6.6 10.8z"/>
          </svg>
          <span>(401) 555-3726</span>
        </div>
      </address>
    </header>

    <section class="recipient">
      <div>Mr. Alan Whitby</div>
      <div>President</div>
      <div>Meridian Ledger Partners</div>
      <div>111 Street Name,</div>
      <div>City State, 12345</div>
    </section>

    <p class="salutation">Dear :</p>

    <div class="letter-body">
      <p>Lorem ipsum dolor sit amet, consectetur adipiscing elit. Aenean ut ipsum eget massa hendrerit vestibulum vel in velit. Donec pretium neque velit.</p>
      <p>Aliquam porta lectus nec mauris ornare venenatis. Vivamus non est turpis, et cursus sem. Mauris vehicula erat in diam auctor at bibendum nisl lacinia.</p>
      <p>Morbi imperdiet neque vehicula nunc convallis gravida. Vestibulum iaculis pretium placerat. Integer consequat, est sit amet facilisis eleifend, nibh nibh varius orci, eget dapibus arcu dui non purus. Pellentesque in magna mauris. Duis enim sapien, dictum vitae condimentum a, pulvinar vel lacus. Mauris et molestie nibh. Vestibulum vitae nulla at metus elementum porta sit amet interdum elit. Nulla sollicitudin neque eu nulla volutpat congue.</p>
      <p>Etiam pellentesque, velit id dapibus fermentum, turpis sapien ornare dui, ac tincidunt ligula odio congue purus. Nunc sed ante dui, in porta lectus. Cras nec sem lorem. In hac habitasse platea dictumst. Maecenas id diam quis dui porta tristique. Sed id egestas felis. Donec ullamcorper mattis posuere. Phasellus fermentum eleifend tortor vel dapibus. Vestibulum ante ipsum.</p>
    </div>

    <div class="signature" role="img" aria-label="Handwritten signature"></div>
    <p class="closing">Sincerely,</p>

    <div class="problem-solving-image" role="img" aria-label="Photo of small wooden figures in groups linked by green lines to a central green figure, suggesting problem solving"></div>
  </main>
</body>
</html>
```